Business card for Chiropractic clinics needs reworked / redesigned

The business card in attachment was designed 10 years ago. It is in need of an update.
We have 2 clinics:
HALSPUNT VORDA & HALSPUNT MIRBE
Only one address needs to be on the card for doctors that only work in one clinic and two addresses need to be on the card for the doctors that work in both clinics.

Target Market(s)

patients/referrers

Industry/Entity Type

Medical

Contact Information for Business Card

Logo (in full or zoomed-in)
Clinic Name
Doctor name and title
clinic address, website, tel, email

Font styles to use
Sans Serif

Colors

Designer to choose colors to be used in the design.

Requirements
Must have
• Good contrast/readability
• We like modern minimalistic designs
• The Bcard needs to project our very high standard of proficiency/professionalism
Should not have
• Not curly
• Not to much colours

```html
<!DOCTYPE html>
<html lang="nl">
<head>
<meta charset="utf-8">
<title>Halspunt business card</title>
<link rel="stylesheet" href="https://fonts.googleapis.com/css2?family=Roboto+Condensed:wght@400;700&family=Roboto:wght@400;700&display=swap">
<style>
  :root {
    --page-bg: #e4e4e4;
    --card-light: #fbfbfb;
    --card-dark: #022326;
    --ink: #0d2a2c;
    --muted: #a3a3a3;
    --body-grey: #555555;
    --white: #ffffff;
    --faint: #2a4346;
  }
  * { margin: 0; padding: 0; box-sizing: border-box; }
  html, body {
    width: 1200px; height: 960px; overflow: hidden;
    background: var(--page-bg);
    font-family: "Roboto", Arial, sans-serif;
  }
  .card {
    position: absolute; left: 312px; width: 600px; height: 343px; overflow: hidden;
  }
  .card--front { top: 113px; background: var(--card-light); }
  .card--back { top: 472px; background: var(--card-dark); color: var(--white); }

  .tab { position: absolute; left: 0; width: 18px; height: 20px; background: var(--ink); }
  .tab--1 { top: 224px; } .tab--2 { top: 248px; } .tab--3 { top: 273px; }

  .identity { position: absolute; left: 69px; top: 223px; }
  .identity__name {
    font-family: "Roboto Condensed", Arial, sans-serif; font-weight: 700;
    font-size: 21px; color: var(--ink); letter-spacing: 0.2px; line-height: 26px;
  }
  .identity__role {
    font-family: "Roboto Condensed", Arial, sans-serif;
    font-size: 15px; color: var(--muted); line-height: 20px; margin-top: 1px;
  }
  .identity__number { font-size: 17px; color: var(--body-grey); line-height: 24px; margin-top: 2px; }

  .brand {
    position: absolute; left: 440px; top: 150px;
    display: flex; align-items: center; gap: 8px;
    font-family: "Roboto Condensed", Arial, sans-serif; font-weight: 700;
    font-size: 20px; letter-spacing: 1px; color: var(--ink);
  }
  .brand__mark { width: 12px; height: 12px; background: var(--ink); }

  .brand-watermark {
    position: absolute; left: 30px; top: 30px;
    font-family: "Roboto Condensed", Arial, sans-serif; font-weight: 700;
    font-size: 44px; letter-spacing: 2px; color: var(--faint);
  }

  .clinic { position: absolute; top: 194px; font-size: 14px; line-height: 19.5px; }
  .clinic--vorda { left: 57px; }
  .clinic--mirbe { left: 348px; }
  .clinic__name { font-weight: 700; }
  .clinic__address { margin-bottom: 5px; }
  .clinic__line { display: flex; align-items: center; gap: 7px; }
  .clinic__line svg { width: 14px; height: 14px; flex: none; fill: var(--white); }
</style>
</head>
<body>
  <section class="card card--front">
    <span class="tab tab--1"></span><span class="tab tab--2"></span><span class="tab tab--3"></span>
    <div class="identity">
      <p class="identity__name">PIETER LANSSENS D.C.</p>
      <p class="identity__role">CHIROPRACTOR</p>
      <p class="identity__number">0.92375.14.000</p>
    </div>
    <div class="brand"><span class="brand__mark"></span>HALSPUNT</div>
  </section>

  <section class="card card--back">
    <div class="brand-watermark">HALSPUNT</div>

    <div class="clinic clinic--vorda">
      <p class="clinic__name">Halspunt Vorda</p>
      <p class="clinic__address">Beukenlaan 118, 9000 Vorda</p>
      <p class="clinic__line"><svg viewBox="0 0 16 16"><path d="M3.5 1.5l2.3-.3 1.3 3.2-1.6 1.2c.8 1.8 2.1 3.1 3.9 3.9l1.2-1.6 3.2 1.3-.3 2.3c-.1.8-.8 1.3-1.6 1.3C6.600 14.600 1.400 9.400 1.400 3.100c0-.8.500-1.500 1.300-1.600z"/></svg>+32 (0)9 456.18.20</p>
      <p class="clinic__line"><svg viewBox="0 0 16 16"><path d="M1 4h14v1L8 9 1 5z"/><path d="M1 6.5l7 4 7-4V12H1z"/></svg>info@halspuntvorda.be</p>
      <p class="clinic__line"><svg viewBox="0 0 16 16"><circle cx="8" cy="8" r="6.5"/><path d="M5 4.5c1.500.5 1.500 2 3 2.500s.5 2-1 2.500-1 2.500-1 3M11 5c-1 1 0 2 1 2.500" stroke="#022326" stroke-width="1.3" fill="none"/></svg>www.halspuntvorda.be</p>
    </div>

    <div class="clinic clinic--mirbe">
      <p class="clinic__name">Halspunt Mirbe</p>
      <p class="clinic__address">Kerkstraat 27</p>
      <p class="clinic__line"><svg viewBox="0 0 16 16"><path d="M3.5 1.5l2.3-.3 1.3 3.2-1.6 1.2c.8 1.8 2.1 3.1 3.9 3.9l1.2-1.6 3.2 1.3-.3 2.3c-.1.8-.8 1.3-1.6 1.3C6.600 14.600 1.400 9.400 1.400 3.100c0-.8.500-1.500 1.300-1.600z"/></svg>+32 (0)9 482.90.41</p>
      <p class="clinic__line"><svg viewBox="0 0 16 16"><path d="M1 4h14v1L8 9 1 5z"/><path d="M1 6.5l7 4 7-4V12H1z"/></svg>info@halspuntmirbe.be</p>
      <p class="clinic__line"><svg viewBox="0 0 16 16"><circle cx="8" cy="8" r="6.5"/><path d="M5 4.5c1.500.5 1.500 2 3 2.500s.5 2-1 2.500-1 2.500-1 3M11 5c-1 1 0 2 1 2.500" stroke="#022326" stroke-width="1.3" fill="none"/></svg>www.halspuntmirbe.be</p>
    </div>
  </section>
</body>
</html>
```